Hoofcare business card

I would like to create a business card design for my hoofcare business.

Front Side- would like to just include the logo and text as per the uploaded files- text font to match logo (upper and lower case).

Back side
- Include the details and contact information provided on the uploaded file.
- Also included on the back side- the uploaded TRUMV logo- keep it small on a top or bottom corner
- for facebook and Instagram contacts- please use the logos next to my usernames

```html
<!DOCTYPE html>
<html lang="en">
<head>
<meta charset="utf-8">
<title>Kestrel Barefoot – Business Card</title>
<link rel="stylesheet" href="https://fonts.googleapis.com/css2?family=Cinzel:wght@400&family=Arimo:wght@400&display=swap">
<style>
  :root {
    --backdrop: #e6e6e4;
    --card: #2f2f2f;
    --ink: #ffffff;
    --ink-soft: #e9e9e9;
    --rule: #d8d8d8;
    --badge: #f2f2f2;
    --serif: "Cinzel", "Times New Roman", serif;
    --sans: "Arimo", Arial, sans-serif;
  }
  * { box-sizing: border-box; margin: 0; padding: 0; }
  html, body { width: 1200px; height: 801px; overflow: hidden; }
  body {
    background: var(--backdrop);
    position: relative;
    font-family: var(--sans);
    color: var(--ink);
  }
  .card {
    position: absolute;
    top: 245px;
    width: 540px;
    height: 310px;
    background: var(--card);
    box-shadow: 0 6px 18px rgba(0,0,0,.22);
    overflow: hidden;
  }
  .card--details { left: 40px; }
  .card--front { left: 620px; }

  /* Details side */
  .card--details .horse-decor {
    position: absolute;
    right: 40px; top: 20px;
    width: 210px; height: 190px;
  }
  .holder-name {
    position: absolute;
    right: 160px; top: 34px;
    font-family: var(--serif);
    font-size: 21px;
    letter-spacing: 1.5px;
    font-variant: small-caps;
  }
  .cert-badge {
    position: absolute;
    right: 30px; top: 92px;
    width: 62px; height: 62px;
  }
  .brand-name {
    position: absolute;
    left: 30px; top: 148px;
    display: flex;
    align-items: center;
    gap: 8px;
    font-family: var(--sans);
    font-weight: 400;
    font-size: 20px;
    line-height: 1.15;
    color: var(--ink);
  }
  .brand-name .dot {
    width: 10px; height: 10px;
    background: var(--ink);
    border-radius: 50%;
    flex: none;
  }
  .contact-list {
    position: absolute;
    left: 200px; top: 130px;
    list-style: none;
    font-size: 14px;
    line-height: 22px;
  }
  .contact-list li { display: flex; align-items: center; gap: 8px; }
  .contact-list svg { width: 12px; height: 12px; flex: none; }
  .contact-list .social-square {
    width: 11px; height: 11px;
    background: var(--ink);
    border-radius: 2px;
    flex: none;
  }
  .details-rule {
    position: absolute;
    left: 200px; right: 40px; top: 232px;
    height: 1px;
    background: var(--rule);
  }
  .service-line {
    position: absolute;
    left: 200px; top: 244px;
    font-size: 14px;
    line-height: 20px;
    color: var(--ink-soft);
  }

  /* Front side */
  .card--front .horse-emboss {
    position: absolute;
    left: 0; top: 40px;
    width: 200px; height: 270px;
  }
  .front-brand {
    position: absolute;
    right: 40px; top: 92px;
    text-align: right;
    font-family: var(--sans);
    font-weight: 400;
    font-size: 36px;
    line-height: 1.1;
  }
  .front-tagline {
    position: absolute;
    right: 40px; top: 186px;
    text-align: right;
    font-size: 15px;
    line-height: 20px;
    color: var(--ink-soft);
  }
</style>
</head>
<body>

  <section class="card card--details" aria-label="Card back with contact details">
    <svg class="horse-decor" role="img" aria-label="Faint horse-head line art decoration" viewBox="0 0 210 190">
      <defs>
        <radialGradient id="decorGlow" cx="50%" cy="45%" r="55%">
          <stop offset="0%" stop-color="#383838"/>
          <stop offset="100%" stop-color="#2f2f2f"/>
        </radialGradient>
      </defs>
      <rect width="210" height="190" fill="url(#decorGlow)"/>
    </svg>

    <div class="holder-name">Mara Linden</div>

    <svg class="cert-badge" viewBox="0 0 62 62" aria-label="Certification badge">
      <circle cx="31" cy="31" r="29" fill="var(--badge)" stroke="#111" stroke-width="3"/>
    </svg>

    <div class="brand-name"><span class="dot"></span><span>Kestrel<br>Barefoot</span></div>

    <ul class="contact-list">
      <li>
        <svg viewBox="0 0 24 24" aria-hidden="true"><path fill="#fff" d="M6.6 10.8a15.1 15.1 0 0 0 6.6 6.6l2.2-2.2c.3-.3.7-.4 1-.2 1.1.4 2.3.6 3.6.6.6 0 1 .4 1 1V20c0 .6-.4 1-1 1A17 17 0 0 1 3 4c0-.6.4-1 1-1h3.5c.6 0 1 .4 1 1 0 1.3.2 2.5.6 3.6.1.3 0 .7-.2 1z"/></svg>
        0411256390
      </li>
      <li>
        <svg viewBox="0 0 24 24" aria-hidden="true"><rect x="2" y="5" width="20" height="14" fill="#fff"/><path d="M2 5l10 8 10-8" fill="none" stroke="#2f2f2f" stroke-width="2"/></svg>
        kestrelbarefoot@mailbox.com
      </li>
      <li><span class="social-square"></span>Kestrel Barefoot</li>
      <li><span class="social-square"></span>kestrelbarefoot</li>
    </ul>

    <div class="details-rule"></div>
    <p class="service-line">Equine Barefoot Trimming And Rehabilitation<br>For All Horses, Ponies And Donkeys.</p>
  </section>

  <section class="card card--front" aria-label="Card front">
    <svg class="horse-emboss" role="img" aria-label="Large embossed horse-head line art decoration" viewBox="0 0 200 270">
      <defs>
        <linearGradient id="embossFade" x1="0" y1="0" x2="1" y2="1">
          <stop offset="0%" stop-color="#3c3c3c"/>
          <stop offset="60%" stop-color="#454545"/>
          <stop offset="100%" stop-color="#303030"/>
        </linearGradient>
      </defs>
      <rect width="200" height="270" fill="url(#embossFade)"/>
    </svg>

    <div class="front-brand">Kestrel<br>Barefoot</div>
    <p class="front-tagline">Equine Barefoot Trimming And Rehabilitation<br>Moreton Bay And Surrounds</p>
  </section>

</body>
</html>
```